RJ's Sports Bar Menu (Harbor Bend Sports Bar)

We are a new england sports bar based on Cape Cod.

We are an old school type sports bar with pizza and wings type food.

We want to highlight our pizza as the main draw on our menu.

The style we are looking for is a placemat menu that looks casual and fun.

We want the following sections:
Starters:

Soups:

Salads:

Handhelds:

Plates:

Sides:

Desserts:

I can provide a draft of all the menu items upon request didn't want to overload this text box thank you!

Requirements
Must have
• The menu must be LANDSCAPE design as it is going on a paper placemat. It also needs to all fit on ONE SIDE.

```html
<!DOCTYPE html>
<html lang="en">
<head>
<meta charset="utf-8">
<title>RJ's Sports Bar — Placemat Menu</title>
<link href="https://fonts.googleapis.com/css2?family=Almendra+SC&family=Montserrat:wght@300;400;600&display=swap" rel="stylesheet">
<style>
  :root {
    --backdrop: #a9a9a9;
    --placemat: #0b0b0b;
    --heading: #f4e600;
    --text: #f2f2f2;
    --leader: #9a9a9a;
    --photo-dark: #17110d;
    --photo-mid: #6e3a1e;
    --photo-warm: #b9763a;
  }
  * { box-sizing: border-box; margin: 0; padding: 0; }
  html, body { width: 1200px; height: 1200px; overflow: hidden; }
  body { background: var(--backdrop); position: relative; font-family: "Montserrat", sans-serif; }

  .placemat {
    position: absolute; left: 61px; top: 220px;
    width: 1079px; height: 760px;
    background: var(--placemat);
    overflow: hidden;
  }

  .pizza-photo {
    position: absolute; left: 705px; top: 232px; width: 374px; height: 528px;
    background: linear-gradient(160deg, var(--photo-dark) 0%, var(--photo-mid) 45%, var(--photo-warm) 75%, var(--photo-mid) 100%);
    z-index: 0;
  }

  .menu-section { position: absolute; width: 305px; height: 200px; z-index: 1; }
  .col-left { left: 32px; }
  .col-right { left: 389px; }

  .section-title {
    font-family: "Almendra SC", serif;
    color: var(--heading);
    font-size: 24px; line-height: 22px;
    letter-spacing: 0.5px;
  }
  .title-arrow { display: block; width: 148px; height: 10px; margin-top: 3px; }

  .item-list { list-style: none; position: absolute; left: 0; right: 0; top: var(--list-offset, 51px); }
  .menu-item {
    display: flex; align-items: baseline;
    color: var(--text); font-weight: 300;
    font-size: 15px; line-height: 18.75px;
  }
  .item-leader { flex: 1; border-bottom: 1px dotted var(--leader); margin: 0 3px; transform: translateY(-3px); }

  .brand {
    position: absolute; left: 770px; top: 84px; width: 266px;
    text-align: center;
    font-family: "Montserrat", sans-serif; font-weight: 600;
    color: var(--text); font-size: 44px; line-height: 52px;
    z-index: 1;
  }
</style>
</head>
<body>
<svg width="0" height="0" style="position:absolute">
  <defs>
    <symbol id="arrow" viewBox="0 0 150 10">
      <path d="M0 5 Q40 2 128 4 L128 1 L150 5 L128 9 L128 6 Q40 8 0 5 Z" fill="#ffffff"/>
    </symbol>
  </defs>
</svg>

<main class="placemat">
  <div class="pizza-photo" role="img" aria-label="Overhead photo of a sliced pizza topped with tomatoes, mushrooms and basil on a dark table with garlic and onion rings"></div>

  <h1 class="brand">RJ's<br>Sports Bar</h1>

  <section class="menu-section col-left" style="top:31px; --list-offset:51px">
    <h2 class="section-title">Starters:</h2>
    <svg class="title-arrow"><use href="#arrow"/></svg>
    <ul class="item-list">
      <li class="menu-item"><span>StartersStartersStarter</span><span class="item-leader"></span><span>$60</span></li>
      <li class="menu-item"><span>StartersStartersStarter</span><span class="item-leader"></span><span>$60</span></li>
      <li class="menu-item"><span>StartersStartersStarter</span><span class="item-leader"></span><span>$60</span></li>
      <li class="menu-item"><span>StartersStartersStarter</span><span class="item-leader"></span><span>$60</span></li>
      <li class="menu-item"><span>StartersStartersStarter</span><span class="item-leader"></span><span>$60</span></li>
      <li class="menu-item"><span>StartersStartersStarter</span><span class="item-leader"></span><span>$60</span></li>
    </ul>
  </section>

  <section class="menu-section col-left" style="top:215px; --list-offset:52px">
    <h2 class="section-title">Soups:</h2>
    <svg class="title-arrow"><use href="#arrow"/></svg>
    <ul class="item-list">
      <li class="menu-item"><span>StartersStartersStarter</span><span class="item-leader"></span><span>$60</span></li>
      <li class="menu-item"><span>StartersStartersStarter</span><span class="item-leader"></span><span>$60</span></li>
      <li class="menu-item"><span>StartersStartersStarter</span><span class="item-leader"></span><span>$60</span></li>
      <li class="menu-item"><span>StartersStartersStarter</span><span class="item-leader"></span><span>$60</span></li>
      <li class="menu-item"><span>StartersStartersStarter</span><span class="item-leader"></span><span>$60</span></li>
      <li class="menu-item"><span>StartersStartersStarter</span><span class="item-leader"></span><span>$60</span></li>
    </ul>
  </section>

  <section class="menu-section col-left" style="top:401px; --list-offset:41px">
    <h2 class="section-title">Salads:</h2>
    <svg class="title-arrow"><use href="#arrow"/></svg>
    <ul class="item-list">
      <li class="menu-item"><span>StartersStartersStarter</span><span class="item-leader"></span><span>$60</span></li>
      <li class="menu-item"><span>StartersStartersStarter</span><span class="item-leader"></span><span>$60</span></li>
      <li class="menu-item"><span>StartersStartersStarter</span><span class="item-leader"></span><span>$60</span></li>
      <li class="menu-item"><span>StartersStartersStarter</span><span class="item-leader"></span><span>$60</span></li>
      <li class="menu-item"><span>StartersStartersStarter</span><span class="item-leader"></span><span>$60</span></li>
      <li class="menu-item"><span>StartersStartersStarter</span><span class="item-leader"></span><span>$60</span></li>
    </ul>
  </section>

  <section class="menu-section col-left" style="top:578px; --list-offset:40px">
    <h2 class="section-title">Handhelds:</h2>
    <ul class="item-list">
      <li class="menu-item"><span>StartersStartersStarter</span><span class="item-leader"></span><span>$60</span></li>
      <li class="menu-item"><span>StartersStartersStarter</span><span class="item-leader"></span><span>$60</span></li>
      <li class="menu-item"><span>StartersStartersStarter</span><span class="item-leader"></span><span>$60</span></li>
      <li class="menu-item"><span>StartersStartersStarter</span><span class="item-leader"></span><span>$60</span></li>
      <li class="menu-item"><span>StartersStartersStarter</span><span class="item-leader"></span><span>$60</span></li>
      <li class="menu-item"><span>StartersStartersStarter</span><span class="item-leader"></span><span>$60</span></li>
    </ul>
  </section>

  <section class="menu-section col-right" style="top:31px; --list-offset:51px">
    <h2 class="section-title">Plates:</h2>
    <svg class="title-arrow"><use href="#arrow"/></svg>
    <ul class="item-list">
      <li class="menu-item"><span>StartersStartersStarter</span><span class="item-leader"></span><span>$60</span></li>
      <li class="menu-item"><span>StartersStartersStarter</span><span class="item-leader"></span><span>$60</span></li>
      <li class="menu-item"><span>StartersStartersStarter</span><span class="item-leader"></span><span>$60</span></li>
      <li class="menu-item"><span>StartersStartersStarter</span><span class="item-leader"></span><span>$60</span></li>
      <li class="menu-item"><span>StartersStartersStarter</span><span class="item-leader"></span><span>$60</span></li>
      <li class="menu-item"><span>StartersStartersStarter</span><span class="item-leader"></span><span>$60</span></li>
    </ul>
  </section>

  <section class="menu-section col-right" style="top:225px; --list-offset:51px">
    <h2 class="section-title">Sides:</h2>
    <svg class="title-arrow"><use href="#arrow"/></svg>
    <ul class="item-list">
      <li class="menu-item"><span>StartersStartersStarter</span><span class="item-leader"></span><span>$60</span></li>
      <li class="menu-item"><span>StartersStartersStarter</span><span class="item-leader"></span><span>$60</span></li>
      <li class="menu-item"><span>StartersStartersStarter</span><span class="item-leader"></span><span>$60</span></li>
      <li class="menu-item"><span>StartersStartersStarter</span><span class="item-leader"></span><span>$60</span></li>
      <li class="menu-item"><span>StartersStartersStarter</span><span class="item-leader"></span><span>$60</span></li>
      <li class="menu-item"><span>StartersStartersStarter</span><span class="item-leader"></span><span>$60</span></li>
    </ul>
  </section>

  <section class="menu-section col-right" style="top:419px; --list-offset:51px">
    <h2 class="section-title">Desserts:</h2>
    <svg class="title-arrow"><use href="#arrow"/></svg>
    <ul class="item-list">
      <li class="menu-item"><span>StartersStartersStarter</span><span class="item-leader"></span><span>$60</span></li>
      <li class="menu-item"><span>StartersStartersStarter</span><span class="item-leader"></span><span>$60</span></li>
      <li class="menu-item"><span>StartersStartersStarter</span><span class="item-leader"></span><span>$60</span></li>
      <li class="menu-item"><span>StartersStartersStarter</span><span class="item-leader"></span><span>$60</span></li>
      <li class="menu-item"><span>StartersStartersStarter</span><span class="item-leader"></span><span>$60</span></li>
      <li class="menu-item"><span>StartersStartersStarter</span><span class="item-leader"></span><span>$60</span></li>
    </ul>
  </section>
</main>
</body>
</html>
```